Menu Design Project for an Italian cafe

Casual Italian style cafe situated in Chinatown in Sydney Australia . Value for money food, good coffee and good location are the cafes strengths. Catering to bushiness crowd in the morning/lunch, tourist crowd for brunch and Asian customers for late afternoon coffee.
Design concept is understated, casual European chic. Should communicate a casual escape to have a good meet up with friends to escape the hustle and bustle of the city crowd.
Would like to move away from current colors of dark brown, creme, black and orange. Would like a more enticing vibrant and brighter colour scheme.
Industry/Entity Type
Cafe
Look and feel
Each slider illustrates characteristics of the customer's brand and the style your logo design should communicate.

```html
<!DOCTYPE html>
<html lang="en">
<head>
<meta charset="utf-8">
<title>Lume Cafe — Dinner Menu</title>
<link rel="stylesheet" href="https://fonts.googleapis.com/css2?family=Oswald:wght@300;400;600&family=Crimson+Text:wght@400&family=Josefin+Sans:wght@700&display=swap">
<style>
  :root {
    --backdrop: #e9e7e3;
    --paper: #fdfcfa;
    --ink: #2b2a29;
    --ink-soft: #4a4846;
    --rule: #e7a9a4;
    --accent: #d9574f;
    --sage: #6f9a7c;
  }
  * { box-sizing: border-box; margin: 0; padding: 0; }
  html, body { width: 1200px; height: 900px; overflow: hidden; }
  body {
    background: var(--backdrop);
    display: flex;
    justify-content: center;
    align-items: center;
    color: var(--ink);
  }
  .menu {
    width: 640px;
    height: 860px;
    background: var(--paper);
    box-shadow: 0 2px 10px rgba(0,0,0,.08);
    padding: 34px 48px;
    text-align: center;
  }
  .brand {
    display: flex;
    justify-content: center;
    align-items: center;
    gap: 10px;
    font-family: "Oswald", sans-serif;
    font-weight: 400;
    font-size: 24px;
    letter-spacing: 2px;
    color: var(--accent);
  }
  .brand-dot {
    width: 30px; height: 30px;
    border: 2px solid var(--accent);
    border-radius: 50%;
  }
  .menu-title {
    margin-top: 14px;
    font-family: "Josefin Sans", sans-serif;
    font-weight: 700;
    font-size: 26px;
    letter-spacing: 8px;
  }
  .divider {
    margin-top: 8px;
    font-family: "Oswald", sans-serif;
    color: var(--sage);
    font-size: 14px;
    letter-spacing: 4px;
  }
  .rule { border: 0; border-top: 1px solid var(--rule); margin: 16px 0 0; }
  .section-title {
    margin: 16px 0 18px;
    font-family: "Oswald", sans-serif;
    font-weight: 300;
    font-size: 28px;
    letter-spacing: 6px;
    color: transparent;
    -webkit-text-stroke: 1px var(--ink);
  }
  .columns {
    display: grid;
    grid-template-columns: 1fr 1fr;
    gap: 0 30px;
  }
  .dish { margin-bottom: 14px; }
  .dish-name {
    font-family: "Oswald", sans-serif;
    font-weight: 600;
    font-size: 15px;
    letter-spacing: .5px;
    text-transform: uppercase;
  }
  .dish-desc {
    font-family: "Crimson Text", serif;
    font-size: 15px;
    line-height: 1.2;
    color: var(--ink-soft);
  }
  .mains .dish-name { font-size: 17px; }
</style>
</head>
<body>
  <main class="menu">
    <header>
      <div class="brand"><span class="brand-dot"></span>Lume</div>
      <h1 class="menu-title">DINNER MENU</h1>
      <div class="divider">·•·//·•·</div>
    </header>

    <hr class="rule">
    <section class="starters">
      <h2 class="section-title">STARTERS &amp; SALADS</h2>
      <div class="columns">
        <div class="column">
          <div class="dish"><h3 class="dish-name">Crostinis, pastas, cold starters</h3><p class="dish-desc">walnuts, cheese, walnuts, cheese, walnuts, cheese, w/ walnuts, cheese &amp; walnuts</p></div>
          <div class="dish"><h3 class="dish-name">Country style spreads</h3><p class="dish-desc">walnuts, cheese, walnuts, cheese, walnuts, cheese, w/ walnuts, cheese &amp; walnuts</p></div>
          <div class="dish"><h3 class="dish-name">Penne ragu</h3><p class="dish-desc">picante bread, chilli, meat &amp; armadillo</p></div>
          <div class="dish"><h3 class="dish-name">Picante plate</h3><p class="dish-desc">picante bread, chilli, meat &amp; armadillo</p></div>
          <div class="dish"><h3 class="dish-name">Taco loco</h3><p class="dish-desc">picante bread, chilli,</p></div>
          <div class="dish"><h3 class="dish-name">Picante plate</h3><p class="dish-desc">picante bread, chilli, meat &amp; armadillo</p></div>
        </div>
        <div class="column">
          <div class="dish"><h3 class="dish-name">Picante plate</h3><p class="dish-desc">picante bread, chilli, meat &amp; armadillo</p></div>
          <div class="dish"><h3 class="dish-name">Picante plate and taco</h3><p class="dish-desc">picante bread, chilli, meat &amp; armadillo</p></div>
          <div class="dish"><h3 class="dish-name">Picante plate</h3><p class="dish-desc">picante bread, chilli, meat &amp; armadillo</p></div>
          <div class="dish"><h3 class="dish-name">Picante plate, funghi e prosciutto</h3><p class="dish-desc">picante bread, chilli, meat &amp; armadillo</p></div>
        </div>
      </div>
    </section>

    <hr class="rule">
    <section class="mains">
      <h2 class="section-title">MAIN COURSES</h2>
      <div class="dish"><h3 class="dish-name">Country style spreads</h3><p class="dish-desc">walnuts, cheese, walnuts, cheese, w/ walnuts, cheese &amp; walnuts, cheese</p></div>
      <div class="dish"><h3 class="dish-name">Country style spreads</h3><p class="dish-desc">walnuts, cheese, walnuts, cheese, w/ walnuts, cheese &amp; walnuts, cheese</p></div>
      <div class="dish"><h3 class="dish-name">Traditional style soups for vegetarians</h3><p class="dish-desc">walnuts, cheese, walnuts, cheese, w/ walnuts, cheese &amp; walnuts, cheese</p></div>
    </section>
  </main>
</body>
</html>
```